Korvell Plant Services

We are a heavy diesel mechanical business with additional air con certificates, remapping engine rebuilt

Contact Information for Business Card

Company Name, Director Name, Managing Director, Contact details, email and website

Font styles to use
Serif
Script

```html
<!DOCTYPE html>
<html lang="en">
<head>
<meta charset="utf-8">
<title>Korvell Plant Services – Business Card</title>
<link href="https://fonts.googleapis.com/css2?family=Montserrat:wght@500;600;700;800&display=swap" rel="stylesheet">
<style>
  :root {
    --navy: #2d2b82;
    --navy-deep: #222066;
    --navy-photo-a: #3a3890;
    --navy-photo-b: #26245f;
    --white: #ffffff;
    --silver-a: #f4f4f6;
    --silver-b: #cfd0d6;
    --page: #eeeeef;
    --tag-icon: #26245f;
  }
  * { box-sizing: border-box; margin: 0; padding: 0; }
  html, body {
    width: 1200px; height: 1200px; overflow: hidden;
    background: var(--page);
    font-family: "Montserrat", Arial, sans-serif;
  }
  .canvas { position: relative; width: 1200px; height: 1200px; }

  .card { position: absolute; left: 200px; width: 800px; height: 480px; overflow: hidden; }

  /* Front */
  .card-front { top: 96px; background: var(--navy); }
  .front-photo {
    position: absolute; left: 0; top: 0; width: 477px; height: 100%;
    background: linear-gradient(120deg, var(--navy-photo-a) 0%, var(--navy) 45%, var(--navy-photo-b) 100%);
  }
  .front-photo-right {
    position: absolute; left: 688px; top: 0; width: 112px; height: 100%;
    background: linear-gradient(180deg, var(--navy-photo-a), var(--navy-photo-b));
  }
  .front-band { position: absolute; left: 477px; top: 0; width: 211px; height: 100%; background: var(--white); }

  .front-wordmark {
    position: absolute; left: 84px; top: 72px; color: var(--white);
    font-weight: 800; line-height: 1;
  }
  .front-wordmark .name { display: block; font-size: 52px; letter-spacing: 2px; }
  .front-wordmark .sub { display: block; font-size: 21px; letter-spacing: 1px; margin-top: 8px; }

  .tag { position: absolute; left: 0; width: 92px; }
  .tag svg { display: block; }
  .tag-icon {
    position: absolute; left: 48px; width: 20px; height: 20px; border-radius: 50%;
    background: var(--tag-icon); display: flex; align-items: center; justify-content: center;
  }

  .person { position: absolute; left: 104px; color: var(--white); line-height: 1.1; }
  .person .person-name { font-size: 21px; font-weight: 700; letter-spacing: 0.5px; }
  .person .person-role { font-size: 10px; font-weight: 500; }

  .contact { position: absolute; left: 104px; top: 312px; color: var(--white); font-size: 21px; font-weight: 700; line-height: 32px; letter-spacing: 0.5px; }

  .badge {
    position: absolute; left: 482px; top: 132px; width: 216px; height: 216px;
    border-radius: 50%; background: var(--navy); border: 5px solid var(--white);
    box-shadow: 0 0 0 4px var(--navy);
    display: flex; flex-direction: column; align-items: center; justify-content: center;
    color: var(--white); font-weight: 800; text-align: center; line-height: 1.05;
  }
  .badge .name { font-size: 34px; }
  .badge .sub { font-size: 17px; }

  /* Back */
  .card-back { top: 620px; background: linear-gradient(180deg, var(--silver-a), var(--silver-b)); }
  .back-shape { position: absolute; inset: 0; }
  .back-mark {
    position: absolute; left: 0; top: 160px; width: 800px;
    display: flex; align-items: center; justify-content: center; gap: 16px;
    color: var(--white); font-weight: 800; line-height: 1.05;
  }
  .back-mark .dot { width: 22px; height: 22px; border-radius: 50%; background: var(--white); }
  .back-mark .name { font-size: 50px; display: block; }
  .back-mark .sub { font-size: 24px; display: block; }
</style>
</head>
<body>
<div class="canvas">

  <section class="card card-front">
    <div class="front-photo" role="img" aria-label="Blue-tinted photograph of heavy plant machinery in a workshop"></div>
    <div class="front-photo-right" role="img" aria-label="Continuation of the blue-tinted machinery photograph"></div>
    <div class="front-band"></div>

    <div class="front-wordmark">
      <span class="name">KORVELL</span>
      <span class="sub">PLANT SERVICES</span>
    </div>

    <div class="tag" style="top:196px">
      <svg width="92" height="30" viewBox="0 0 92 30"><path d="M0 0H78L92 15L78 30H0Z" fill="var(--white)"/></svg>
      <span class="tag-icon" style="top:5px">
        <svg width="10" height="10" viewBox="0 0 10 10"><circle cx="5" cy="3" r="2.2" fill="var(--white)"/><path d="M1 10a4 4 0 0 1 8 0Z" fill="var(--white)"/></svg>
      </span>
    </div>
    <div class="person" style="top:193px">
      <div class="person-name">DALE MORROW</div>
      <div class="person-role">Director</div>
    </div>

    <div class="tag" style="top:242px">
      <svg width="92" height="30" viewBox="0 0 92 30"><path d="M0 0H78L92 15L78 30H0Z" fill="var(--white)"/></svg>
      <span class="tag-icon" style="top:5px">
        <svg width="10" height="10" viewBox="0 0 10 10"><circle cx="5" cy="3" r="2.2" fill="var(--white)"/><path d="M1 10a4 4 0 0 1 8 0Z" fill="var(--white)"/></svg>
      </span>
    </div>
    <div class="person" style="top:239px">
      <div class="person-name">REID CALLAN</div>
      <div class="person-role">Managing Director</div>
    </div>

    <div class="tag" style="top:312px">
      <svg width="92" height="64" viewBox="0 0 92 64"><path d="M0 0H78L92 32L78 64H0Z" fill="var(--white)"/></svg>
      <span class="tag-icon" style="top:6px">
        <svg width="11" height="11" viewBox="0 0 24 24"><path d="M6.6 10.8a15 15 0 0 0 6.6 6.6l2.2-2.2a1 1 0 0 1 1-.25 11.4 11.4 0 0 0 3.6.57 1 1 0 0 1 1 1V20a1 1 0 0 1-1 1A17 17 0 0 1 3 4a1 1 0 0 1 1-1h3.5a1 1 0 0 1 1 1c0 1.25.2 2.45.57 3.57a1 1 0 0 1-.25 1Z" fill="var(--white)"/></svg>
      </span>
      <span class="tag-icon" style="top:38px">
        <svg width="11" height="11" viewBox="0 0 24 24"><rect x="2" y="5" width="20" height="14" rx="2" fill="var(--white)"/><path d="M3 6l9 7 9-7" stroke="var(--tag-icon)" stroke-width="2" fill="none"/></svg>
      </span>
    </div>
    <div class="contact">
      <div>0400 555 219</div>
      <div>admin@korvellplant.net</div>
    </div>

    <div class="badge">
      <span class="name">KORVELL</span>
      <span class="sub">Plant Services</span>
    </div>
  </section>

  <section class="card card-back">
    <svg class="back-shape" width="800" height="480" viewBox="0 0 800 480">
      <path d="M0 42H200C240 42 250 64 290 64H800V372H620C580 372 570 398 530 398H0Z" fill="var(--navy)"/>
    </svg>
    <div class="back-mark">
      <span class="dot"></span>
      <span>
        <span class="name">KORVELL</span>
        <span class="sub">Plant Services</span>
      </span>
    </div>
  </section>

</div>
</body>
</html>
```